Independent Midwife for a positive birth experience needs a vibrant, and elegant business card/logo

I need a business card design with a logo. The logo I would like to be able to use on my website (www.midwifeorlaith.com) next to my name.
Therefore the design of the card and logo should suit the colours and design of the website. The title of the website and company is "Orlaith Denby Marsworth, Midwife" but I'd like to have the business card title to be "Orlaith Denby Marsworth - Independent Midwife" in bold letters, same script font as in my website.

I provide gold standard midwifery services, one-to-one tailored care, continuity of care throughout the entire pregnancy (antenatal care), the birth and after the birth (postnatal care), home birth, water birth, breast-feeding support, and birth preparation workshops. I also am certified and offer complementary therapies: pregnancy reflexology, rebozo techniques for optimal baby positioning.

The design should incorporate similar colours and style as the website and the "Orlaith Denby Marsworth - Independent Midwife" on the card should include the same font as in the title of the website, however, in bold. The front of the card should have a logo, title and contact information (phone number 071592604, email orlaith.marsworth@quillpost.com, website address www.midwifeorlaith.com).
The back of the card to include the services I offer.

The logo: use of colour purple (varying shades), should communicate communicate warmth, kindness, compassion. It should convey that I'm a midwife who believes in fostering a trusting relationship with my clients and to provide them with a positive pregnancy and birth experience.

Target Market(s)

Pregnant women or women who are looking to book a private midwife for better birth experience and outcome

Industry/Entity Type

Baby

Contact Information for Business Card

Name and Title on front side together with contact details
The reverse side should have services/packages offered

Font styles to use
Script
Other font styles liked:
• similar script as in my website for name and title, and easy to read font for the rest of the words

Colors
b768aa
a54599
d2a4cc
ffffff

Requirements
Must have
• same font as title of website, but slightly bolder.
• similar design, colours, patterns as in website.
• Also include a gold accent colour somewhere in the design please.
Nice to have
• perhaps a logo of pregnant belly in profile or newborn baby icon

```html
<!DOCTYPE html>
<html lang="en">
<head>
<meta charset="utf-8">
<title>Orlaith Denby Marsworth - Independent Midwife · Business Card</title>
<link rel="stylesheet" href="https://fonts.googleapis.com/css2?family=Parisienne&family=Cabin:wght@400;700&display=swap">
<style>
  :root {
    --plum: #a54599;
    --plum-deep: #9b2d8a;
    --orchid: #b768aa;
    --lilac: #d2a4cc;
    --gold-text: #c4b83a;
    --gold-light: #f2e36a;
    --gold-dark: #8a5a12;
    --paper: #ffffff;
    --edge: #3a3a3a;
  }
  * { margin: 0; padding: 0; box-sizing: border-box; }
  html, body { width: 1200px; height: 900px; overflow: hidden; background: var(--paper); }
  body { position: relative; font-family: "Cabin", "Gill Sans", sans-serif; }

  .card {
    position: absolute;
    left: 254px;
    width: 691px;
    height: 401px;
    border: 1px solid var(--edge);
    background: var(--paper);
    overflow: hidden;
  }
  .card--front { top: 37px; }
  .card--back { top: 458px; }
  .card__corner { position: absolute; inset: 0; width: 100%; height: 100%; }

  .brand-mark {
    position: absolute;
    left: 22px; top: 120px;
    display: flex; align-items: center; gap: 10px;
    color: var(--orchid);
    font-size: 22px;
    font-weight: 400;
  }
  .brand-mark__dot {
    width: 18px; height: 18px; border-radius: 50%;
    background: var(--lilac);
  }

  .title {
    position: absolute;
    font-family: "Parisienne", cursive;
    color: var(--plum-deep);
    white-space: nowrap;
    font-weight: 400;
  }
  .title__name { left: 201px; top: 128px; font-size: 38px; }
  .title__role { left: 276px; top: 192px; font-size: 29px; }

  .contact {
    position: absolute;
    left: 150px; top: 261px;
    display: grid;
    grid-template-columns: 108px 1px auto;
    column-gap: 15px;
    font-size: 17px;
    line-height: 22.5px;
  }
  .contact__labels { text-align: right; color: var(--gold-text); font-weight: 700; }
  .contact__rule { background: linear-gradient(var(--lilac), transparent); }
  .contact__values { color: var(--orchid); padding-bottom: 20px; }

  .services {
    position: absolute;
    left: 278px; top: 99px;
    list-style: none;
    color: var(--plum-deep);
    font-size: 21px;
    line-height: 29.6px;
  }
</style>
</head>
<body>

<section class="card card--front" aria-label="Business card front">
  <svg class="card__corner" viewBox="0 0 691 401" aria-hidden="true">
    <defs>
      <linearGradient id="goldFront" x1="0" y1="1" x2="1" y2="0">
        <stop offset="0" stop-color="var(--gold-dark)"/>
        <stop offset="0.45" stop-color="var(--gold-light)"/>
        <stop offset="1" stop-color="var(--gold-dark)"/>
      </linearGradient>
    </defs>
    <path d="M691,205 C684,320 620,385 500,401 L691,401 Z" fill="url(#goldFront)"/>
    <path d="M691,258 C680,345 630,390 546,401 L691,401 Z" fill="var(--plum)"/>
  </svg>

  <div class="brand-mark">
    <span class="brand-mark__dot"></span>
    <span>Orlaith</span>
  </div>

  <h1 class="title title__name">Orlaith Denby Marsworth</h1>
  <h2 class="title title__role">Independent Midwife</h2>

  <div class="contact">
    <div class="contact__labels">phone<br>email<br>website</div>
    <div class="contact__rule"></div>
    <div class="contact__values">071592604<br>orlaith.marsworth@quillpost.com<br>www.midwifeorlaith.com</div>
  </div>
</section>

<section class="card card--back" aria-label="Business card back">
  <svg class="card__corner" viewBox="0 0 691 401" aria-hidden="true">
    <defs>
      <linearGradient id="goldBack" x1="1" y1="1" x2="0" y2="0">
        <stop offset="0" stop-color="var(--gold-dark)"/>
        <stop offset="0.45" stop-color="var(--gold-light)"/>
        <stop offset="1" stop-color="var(--gold-dark)"/>
      </linearGradient>
    </defs>
    <path d="M0,212 C8,320 70,385 200,401 L0,401 Z" fill="url(#goldBack)"/>
    <path d="M0,262 C10,345 60,390 150,401 L0,401 Z" fill="var(--plum)"/>
  </svg>

  <ul class="services">
    <li>Gold Standard Midwifery Services</li>
    <li>One-to-one tailored care</li>
    <li>Antenatal care</li>
    <li>Postnatal care</li>
    <li>Home Birth &amp; Water Birth</li>
    <li>Breast-feeding support</li>
    <li>Birth preparation workshops</li>
    <li>Certified in complementary therapies</li>
  </ul>
</section>

</body>
</html>
```